Postcard Design for Direct Mail Campaign for PIttsburgh area attorney

I am an attorney in Pittsburgh, I did this before and selected three designs. I am not sure if those responding can see which three I selected. Those designs are in use now. All 3 go out. The issue is they cost the standard mailing rate and I will use all 3 of those forever. There will be times I would like to take advantage of the postcard mailing rate and thus this one is smaller. I want the postcard to emphasize I do criminal and SOME civil law. See my sites www.brookvaledefenselaw.com and www.tovacounsel.net.

IN FACT I AM PUTTING THE THREE I AM MAILING RIGHT NOW IN THE IMAGES> I TRUST THAT THESE WILL BE USED TO INSPIRE AND GUIDE AND NO COPY. i Cannot upload those images. You can probably see my 3 winners.

Target Market(s)

Pittsburgh area people who may need a criminal attorney or a civil attorney.

Industry/Entity Type

Legal

Colors
ec1f27

Requirements
Must have
• A balanced criminal - civil thing as these are going to people in the mail with no envelope.
Nice to have
• On my site www.brookvaledefenselaw.com I have badges in the sidebar.
Should not have
• People being arrested. I am putting up new images.

```html
<!DOCTYPE html>
<html lang="en">
<head>
<meta charset="utf-8">
<title>Daniel R. Hartwell – Postcard</title>
<link rel="stylesheet" href="https://fonts.googleapis.com/css2?family=Cinzel:wght@400;500&family=Barlow:wght@400;500;700&family=Oswald:wght@400;500&family=Open+Sans:wght@400;700&display=swap">
<style>
  :root{
    --red:#d2222b;
    --gold:#c99a3c;
    --cream:#ede9d8;
    --dark:#232323;
    --ink:#1f1f1f;
    --blue:#1e84c6;
    --navy:#1b4f8a;
    --yellow:#f4c21a;
    --white:#ffffff;
  }
  *{margin:0;padding:0;box-sizing:border-box}
  html,body{width:1200px;height:1200px;overflow:hidden;background:var(--white)}
  .canvas{position:relative;width:1200px;height:1200px}
  .abs{position:absolute}

  /* front side */
  .front{left:244px;top:71px;width:716px;height:483px}
  .front-main{left:0;top:0;width:474px;height:483px;background:var(--cream)}
  .band-top{left:0;top:0;width:474px;height:17px;background:var(--red)}
  .header{left:0;top:34px;width:474px;height:107px;background:var(--red);border-bottom:6px solid var(--gold);color:var(--white);font-family:'Cinzel',serif;padding:22px 0 0 56px}
  .header .pre{font-size:19px;letter-spacing:.5px}
  .header .name{font-size:27px;line-height:1.05;letter-spacing:.5px}
  .header .tag{font-size:11.5px;margin-top:6px;letter-spacing:.2px}
  .band-bottom{left:0;top:460px;width:474px;height:23px;background:var(--red);border-top:5px solid var(--gold)}
  .offer{left:56px;top:162px;font-family:'Barlow',sans-serif}
  .offer .lead{font-weight:700;font-size:16px;color:var(--ink);letter-spacing:.3px}
  .offer ul{list-style:none;margin-top:2px}
  .offer li{font-size:15.5px;line-height:20px;color:var(--blue)}
  .offer .claim{font-weight:700;font-size:15.5px;line-height:20px;color:var(--ink);margin-top:8px}
  .photo-frame{left:367px;top:173px;width:108px;height:257px;border:2px solid var(--gold);background:var(--white);padding:3px}
  .ph{position:absolute}
  .ph-attorney{left:3px;top:3px;width:98px;height:134px;background:linear-gradient(160deg,#9fb3c6,#5a6f86)}
  .ph-gavel{left:3px;top:141px;width:48px;height:44px;background:linear-gradient(160deg,#c9a878,#6d5236)}
  .ph-car{left:53px;top:141px;width:48px;height:44px;background:linear-gradient(160deg,#8a8f96,#2e3238)}
  .ph-stop{left:3px;top:189px;width:98px;height:60px;background:linear-gradient(160deg,#7d8794,#3a414a)}
  .badges{left:49px;top:396px;display:flex;gap:9px;align-items:center}
  .badge{width:44px;height:44px;border-radius:50%}
  .badge.b1{background:#2d4e87}
  .badge.b2{background:#e9eef4;border:3px solid #4a8bc9}
  .badge.b3{background:#5a2f32}
  .badge.b4{width:56px;height:44px;border-radius:3px;background:#e2e6ea;border:2px solid #1f5a92}
  .badge.b5{width:52px;height:38px;border-radius:4px;background:#f2d37a}

  .front-aside{left:486px;top:0;width:230px;height:483px;background:var(--dark);color:var(--white);text-align:center}
  .need{margin-top:22px;font-family:'Oswald',sans-serif;font-size:20px;letter-spacing:.3px}
  .call{font-family:'Oswald',sans-serif;font-size:20px;color:var(--yellow);margin-top:-2px}
  .emblem{width:102px;height:76px;margin:12px auto 0;border-radius:6px;background:radial-gradient(ellipse at 50% 40%,#b8893a 0%,#6e5428 55%,rgba(35,35,35,0) 100%)}
  .review{margin:18px 20px 0 20px;font-family:'Open Sans',sans-serif;font-size:10.2px;line-height:15px;text-align:justify;letter-spacing:.2px;text-transform:uppercase}
  .review b{font-weight:700}

  /* back side */
  .back{left:241px;top:641px;width:719px;height:488px}
  .back-main{left:0;top:0;width:400px;height:488px;background:var(--cream)}
  .ph-family{left:23px;top:25px;width:366px;height:172px;background:linear-gradient(180deg,#d9e2ea 0%,#b7c4cf 45%,#6f9a49 70%,#4f7a32 100%)}
  .summary{left:26px;top:209px;width:170px;font-family:'Barlow',sans-serif;font-size:14.5px;line-height:19.5px;color:var(--navy);text-transform:uppercase}
  .ph-desk{left:199px;top:209px;width:189px;height:110px;background:linear-gradient(160deg,#d4d4d4,#3c3c3c)}
  .guild{left:24px;top:360px;width:110px;text-align:center;font-family:'Barlow',sans-serif;font-weight:700;font-size:14px;line-height:16px;color:var(--navy);text-transform:uppercase}
  .guild .mark{display:block;width:26px;height:26px;background:var(--navy);margin:0 auto 8px}
  .contact{left:200px;top:338px;font-family:'Barlow',sans-serif;color:var(--navy);text-align:center;width:190px}
  .contact .free{font-size:15.5px;text-transform:uppercase;letter-spacing:.2px}
  .contact .num{font-size:15.5px;line-height:28px}
  .contact .num span{font-size:21px}
  .contact .mail{font-size:15.5px;line-height:20px;margin-top:4px}

  .back-address{left:400px;top:0;width:319px;height:488px;border:1.5px solid var(--ink);border-left:none;background:var(--white)}
  .address{left:20px;top:33px;width:152px;text-align:right;white-space:nowrap;font-family:'Barlow',sans-serif;font-size:13px;line-height:16.5px;color:var(--ink);text-transform:uppercase}
  .stamp{left:185px;top:35px;width:105px;height:79px;border:1.5px dashed var(--ink);display:flex;align-items:center;justify-content:center;font-family:'Barlow',sans-serif;font-size:13px;color:var(--ink)}
</style>
</head>
<body>
<div class="canvas">

  <section class="front abs">
    <div class="front-main abs">
      <div class="band-top abs"></div>
      <header class="header abs">
        <div class="pre">The Law Office of</div>
        <div class="name">Daniel R. Hartwell</div>
        <div class="tag">Pittsburgh Criminal Defense-Personal Injury Attorney</div>
      </header>
      <div class="offer abs">
        <div class="lead">25 YEARS’ EXPERIENCE IN</div>
        <ul>
          <li>DUI DEFENSE</li>
          <li>PERSONAL INJURY</li>
          <li>CRIMINAL DEFENSE</li>
          <li>TRAFFIC CITATIONS/LICENSE ISSUES</li>
          <li>APPEALS/ POST-CONVICTION</li>
        </ul>
        <div class="claim">EXTENSIVE EXPERIENCE WITH<br>A PROVEN RECORD OF SUCCESS</div>
        <div class="claim">REASONABLE FEES IN BOTH<br>CRIMINAL AND CIVIL CASES</div>
      </div>
      <div class="photo-frame abs">
        <div class="ph ph-attorney" role="img" aria-label="Attorney in shirt and tie working at his desk"></div>
        <div class="ph ph-gavel" role="img" aria-label="Gavel and scales of justice"></div>
        <div class="ph ph-car" role="img" aria-label="Car on the road"></div>
        <div class="ph ph-stop" role="img" aria-label="Traffic stop at a driver's window"></div>
      </div>
      <div class="badges abs">
        <div class="badge b1" role="img" aria-label="Professional membership badge"></div>
        <div class="badge b2" role="img" aria-label="Review listing badge"></div>
        <div class="badge b3" role="img" aria-label="Trial lawyers association badge"></div>
        <div class="badge b4" role="img" aria-label="Accredited business badge"></div>
        <div class="badge b5" role="img" aria-label="Attorney directory badge"></div>
      </div>
      <div class="band-bottom abs"></div>
    </div>

    <aside class="front-aside abs">
      <div class="need">NEED AN ATTORNEY?</div>
      <div class="call">CALL 412-555-0148</div>
      <div class="emblem" role="img" aria-label="Gold crest emblem for 25 years of experience with scrollwork"></div>
      <p class="review">"***** <b>Daniel</b> is a true savior.. only commits to what he can deliver, and delivers it too. No hidden agendas. Had a case from two years back which my previous attorney had me plead guilty to, stating it was just like a speeding ticket. It came back to bite me now and I could have been deported. Lucky I hired Daniel and he explained his course of action clearly.. and worked out all that in my favor. Another plus was that his fees was far less than what other attorneys charged. Always reachable on phone." Client - Lexrate - 2015</p>
    </aside>
  </section>

  <section class="back abs">
    <div class="back-main abs">
      <div class="ph ph-family" role="img" aria-label="Family of three generations lying on a lawn"></div>
      <p class="summary abs">Over 25 years of expe-<br>rience in criminal<br>defense, DUI defense<br>and personal injury<br>cases. Serving all of<br>Western PA.</p>
      <div class="ph ph-desk" role="img" aria-label="Black and white desk with attorney nameplate"></div>
      <div class="guild abs"><span class="mark"></span>Keystone<br>Bar Guild</div>
      <div class="contact abs">
        <div class="free">For Free Consultation</div>
        <div class="num">CALL: <span>412-555-0148</span></div>
        <div class="num">or <span>412-555-0172</span></div>
        <div class="mail">email: dan@tova-law.net<br>dhartwell@tovacounsel.net</div>
      </div>
    </div>
    <div class="back-address abs">
      <div class="address abs">Daniel R. Hartwell<br>1800 Counsel Tower<br>512 Ridgeline Avenue<br>Pittsburgh, PA 15222<br>Pennsylvania, U.S.A</div>
      <div class="stamp abs">STAMP</div>
    </div>
  </section>

</div>
</body>
</html>
```